Corvane Project Services - Flyer

Project Breif:
I need a single page A4 Capability Statement, which will be used to market our services to prospective clients, both in print and via email PDF.
It needs to look professional and should incorporate the elements I have uploaded into files, these include:
Capability Statement Text
Corvane Services Company Logo
Additional Logo’s (Tools We Use)
Glimmer Bay Pics can be cut into the page
I have included examples of capability statements as a guide to what i am looking for.
Regards
Derek
Engineering Consulting

```html
<!DOCTYPE html>
<html lang="en">
<head>
<meta charset="utf-8">
<title>Corvane Project Services – Capability Statement</title>
<link href="https://fonts.googleapis.com/css2?family=Oswald:wght@400;500&family=Open+Sans:wght@400;600;700&display=swap" rel="stylesheet">
<style>
  :root{
    --backdrop:#d6d7d9;
    --paper:#ffffff;
    --brand-blue:#86a9d6;
    --bullet-blue:#7fc0e8;
    --name-blue:#7a9fcf;
    --navy:#1d3f8a;
    --ink:#2b2b2b;
    --grey-bar:#e6e6e6;
    --photo-a:#dfe6ef;
    --photo-b:#b9cde3;
    --strip:#a9cbe8;
  }
  *{margin:0;padding:0;box-sizing:border-box}
  html,body{width:897px;height:1200px;overflow:hidden;background:var(--backdrop)}
  body{position:relative;font-family:"Open Sans",sans-serif;color:var(--ink)}
  .flyer{position:absolute;left:65px;top:58px;width:768px;height:1085px;background:var(--paper);overflow:hidden}
  .abs{position:absolute}
  .contact-name{left:51px;top:24px;font-family:"Oswald",sans-serif;font-size:24px;color:var(--name-blue);letter-spacing:1px;white-space:nowrap}
  .contact-name small{font-size:17px}
  .phone-bar{left:0;top:61px;width:383px;height:39px;background:var(--grey-bar)}
  .phone-bar svg{position:absolute;left:69px;top:11px}
  .phone-bar span{position:absolute;left:105px;top:5px;font-size:21px;font-weight:700;letter-spacing:1.5px;color:#333}
  .brand{left:523px;top:40px;width:176px;text-align:center}
  .brand-mark{width:46px;height:46px;border-radius:50%;background:var(--navy);margin:0 auto 10px}
  .brand-name{font-size:12px;font-weight:700;color:var(--navy);letter-spacing:1.5px;line-height:1.35}
  .photos{left:0;top:116px}
  .intro-band{left:0;top:332px;width:768px;height:66px;background:var(--brand-blue);color:#fff;text-align:center;font-size:17.5px;letter-spacing:1.2px;line-height:25px;padding-top:8px}
  .intro-band b{font-weight:700}
  .intro-list{left:43px;top:412px;width:700px;list-style:none}
  .intro-list li{position:relative;padding-left:26px;font-size:14.5px;letter-spacing:1px;line-height:19px;margin-bottom:10px}
  .intro-list li::before{content:"";position:absolute;left:0;top:3px;width:13px;height:13px;background:var(--bullet-blue)}
  .core-tab{left:0;top:592px;width:314px;height:52px;background:var(--brand-blue);color:#fff;font-size:24px;letter-spacing:1.5px;padding:10px 0 0 56px}
  .core-tab b{font-size:27px;font-weight:700}
  .service h3{font-size:17.5px;font-weight:600;letter-spacing:1.2px;margin-bottom:8px}
  .service ul{list-style:none}
  .service li{position:relative;padding-left:24px;font-size:14px;letter-spacing:1.1px;height:22.6px;line-height:20px}
  .service li::before{content:"";position:absolute;left:0;top:7px;width:7px;height:7px;background:var(--bullet-blue)}
  .planning{left:50px;top:660px}
  .planning h3{margin-left:19px}
  .cost{left:50px;top:866px}
  .cost h3{margin-left:25px}
  .cost li{height:23.5px}
  .risk{left:414px;top:612px}
  .risk h3{margin-left:25px;margin-bottom:10px}
  .risk li{height:25.6px}
  .tool{font-size:15px;font-weight:700;color:#444;white-space:nowrap;display:flex;align-items:center;gap:6px}
  .tool i{display:inline-block;width:14px;height:14px}
  .footer{left:0;top:1030px;width:768px;height:55px;background:var(--brand-blue);color:#fff;font-size:17px;letter-spacing:1.5px}
  .footer span{position:absolute;top:14px}
  .footer svg{position:absolute;top:19px}
</style>
</head>
<body>
<main class="flyer">
  <div class="abs contact-name">DEREK HALLORAN <small>(MANAGING DIRECTOR)</small></div>
  <div class="abs phone-bar">
    <svg width="20" height="18" viewBox="0 0 24 24"><path fill="#333" d="M6.6 10.8a15 15 0 0 0 6.6 6.6l2.2-2.2a1 1 0 0 1 1-.25 11.4 11.4 0 0 0 3.6.57 1 1 0 0 1 1 1V20a1 1 0 0 1-1 1A17 17 0 0 1 3 4a1 1 0 0 1 1-1h3.5a1 1 0 0 1 1 1c0 1.25.2 2.45.57 3.57a1 1 0 0 1-.25 1z"/></svg>
    <span>+353 (0)874 519 206</span>
  </div>

  <div class="abs brand">
    <div class="brand-mark"></div>
    <div class="brand-name">CORVANE PROJECT<br>SERVICES</div>
  </div>

  <svg class="abs photos" width="768" height="216" viewBox="0 0 768 216">
    <defs>
      <linearGradient id="photoLeft" x1="0" y1="0" x2="1" y2="1"><stop offset="0" stop-color="var(--photo-a)"/><stop offset="1" stop-color="#c9d6e6"/></linearGradient>
      <linearGradient id="photoRight" x1="0" y1="0" x2="1" y2="1"><stop offset="0" stop-color="var(--photo-b)"/><stop offset="1" stop-color="#eef1f5"/></linearGradient>
    </defs>
    <polygon points="318,0 372,0 444,194 410,194" fill="var(--strip)" opacity=".8"/>
    <polygon role="img" aria-label="Photo of a printed project schedule chart with a pen" points="0,0 327,0 419,194 0,194" fill="url(#photoLeft)"/>
    <polygon role="img" aria-label="Photo of colleagues reviewing documents at a desk" points="371,21 768,21 768,216 443,216" fill="url(#photoRight)"/>
  </svg>

  <div class="abs intro-band"><b>Corvane Project Services Ltd</b>. is a leading project control<br>consultancy based in <b>Co Cork Ireland</b></div>

  <ul class="abs intro-list">
    <li>For over <b>20 years</b> we have been helping our clients to deliver complex projects and programs throughout mainland <b>Europe.</b></li>
    <li>We are passionate about empower organisations to achieve their objectives, on time and on budget.</li>
    <li>We are continually innovating, evolving and learning, utilize the latest industry tools and techniques to deliver real value to our clients.</li>
    <li>Our goal is to make successful project delivery more achievable and repeatable.</li>
  </ul>

  <div class="abs core-tab"><b>Core</b> Services:</div>

  <section class="abs service planning">
    <h3>Planning and Scheduling</h3>
    <ul>
      <li>Tender Planning</li>
      <li>Interactive Planning / Pull Planning</li>
      <li>EPCMV Planning &amp; Scheduling</li>
      <li>Schedule Earned Value Management</li>
      <li>Independent Schedule Quality Assessment</li>
      <li>Schedule Risk Analysis (Monte Carlo)</li>
      <li>Training</li>
    </ul>
  </section>

  <section class="abs service cost">
    <h3>Cost Control</h3>
    <ul>
      <li>Estimating &amp; Forecasting</li>
      <li>Change Management</li>
      <li>Earned Value Analysis</li>
      <li>Progress Reporting</li>
      <li>Cost Risk Analysis</li>
    </ul>
  </section>

  <section class="abs service risk">
    <h3>Management of Risk (RiskFrame)</h3>
    <ul>
      <li>Risk Management Policies &amp; Procedures</li>
      <li>Risk Management Strategy</li>
      <li>Risk Registers</li>
      <li>Risk Improvement Planning</li>
      <li>Risk Response and Communication</li>
      <li>Risk Management Training</li>
    </ul>
  </section>

  <div class="abs tool" style="left:436px;top:836px">Orvelle Planner</div>
  <div class="abs tool" style="left:571px;top:838px"><i style="background:#3d8a4a"></i>Taskgrid</div>
  <div class="abs tool" style="left:455px;top:888px"><i style="background:#d8322e"></i>Mastline Planner</div>
  <div class="abs tool" style="left:431px;top:938px">Waypoint Pro</div>
  <div class="abs tool" style="left:573px;top:938px"><i style="background:var(--navy);border-radius:50%"></i>RiskFrame</div>
  <div class="abs tool" style="left:520px;top:990px">Gaugeline</div>

  <footer class="abs footer">
    <svg style="left:93px" width="20" height="15" viewBox="0 0 20 15"><rect x="1" y="1" width="18" height="13" fill="none" stroke="#fff" stroke-width="1.5"/><path d="M1 1l9 7 9-7" fill="none" stroke="#fff" stroke-width="1.5"/></svg>
    <span style="left:128px">info@corvaneservices.ie</span>
    <svg style="left:415px;top:17px" width="20" height="20" viewBox="0 0 20 20"><g fill="none" stroke="#fff" stroke-width="1.4"><circle cx="10" cy="10" r="8.5"/><ellipse cx="10" cy="10" rx="4" ry="8.5"/><path d="M1.5 10h17M3 5.5h14M3 14.5h14"/></g></svg>
    <span style="left:455px">www.corvaneservices.ie</span>
  </footer>
</main>
</body>
</html>
```